Wellpath Ledgers New Website

Please review the attached Design Brief with additional details. Thank you!

The goal is to create a website that effectively communicates the benefits of WellPath Ledgers to eye care professionals. The website should streamline the process of understanding and utilizing WellPath Ledgers' services, emphasizing improved patient outcomes, increased referrals, and enhanced patient engagement.

Target Market(s)

Eyecare Professionals

Number of Pages Required

4 page

```html
<!DOCTYPE html>
<html lang="en">
<head>
<meta charset="utf-8">
<title>Wellpath Ledgers — Medical Registries Services</title>
<link href="https://fonts.googleapis.com/css2?family=Ubuntu:wght@400;500;700&family=Nunito+Sans:wght@400;600;700&display=swap" rel="stylesheet">
<style>
:root{
  --navy:#1f3c68;
  --navy-deep:#18325a;
  --ink:#1c2a44;
  --topbar:#262a3c;
  --orange:#f7a21b;
  --orange-dark:#ee8f12;
  --grey-bg:#f5f5f6;
  --text:#6b7180;
  --line:#d9dde4;
  --white:#ffffff;
}
*{box-sizing:border-box;margin:0;padding:0}
html,body{width:1200px;height:4841px;overflow:hidden}
body{position:relative;background:var(--white);font-family:"Nunito Sans",sans-serif;color:var(--text)}
.abs{position:absolute}
h1,h2,h3,h4{font-family:"Ubuntu",sans-serif;color:var(--navy);font-weight:500}
.eyebrow{position:absolute;font-size:12px;color:var(--orange);letter-spacing:.5px;text-transform:uppercase;text-decoration:underline}
.btn{position:absolute;display:flex;align-items:center;justify-content:center;gap:12px;background:var(--orange);color:#fff;font-family:"Ubuntu",sans-serif;font-weight:500;font-size:15px;border-radius:2px}
.photo{position:absolute}
/* top bar */
.topbar{top:0;left:0;width:1200px;height:45px;background:var(--topbar);color:#d7dae2;font-size:14px}
.topbar span{position:absolute;top:14px}
.social-dot{position:absolute;top:17px;width:11px;height:11px;border-radius:2px;background:#9aa1b3}
/* header */
.header{top:45px;left:0;width:1200px;height:111px;background:#fff}
.brand{position:absolute;display:flex;align-items:center;gap:10px;font-family:"Ubuntu",sans-serif;font-weight:500}
.brand i{display:block;width:22px;height:22px;border-radius:50%;background:var(--orange)}
.contact-chip{position:absolute;font-size:13px;color:#2b3345;line-height:1.7}
.contact-chip small{display:block;font-size:12px;color:#7b8292}
.nav{top:156px;left:79px;width:984px;height:66px;background:#fff;z-index:3;display:flex;align-items:center;font-size:13px;color:#5b6170}
.nav a{position:absolute;top:25px}
.nav .active{color:var(--navy);font-weight:700}
.phone-box{top:156px;left:1065px;width:71px;height:66px;background:var(--navy);z-index:3;display:flex;align-items:center;justify-content:center}
/* hero */
.hero{top:156px;left:0;width:1200px;height:792px;background:linear-gradient(100deg,#1d3356 0%,#2a4670 45%,#3b5a82 70%,#24405f 100%)}
.hero-tag{top:451px;left:100px;width:266px;height:41px;background:#2e4c7c;border-left:4px solid var(--orange);color:#fff;font-family:"Ubuntu",sans-serif;font-weight:700;font-size:20px;padding:8px 18px}
.hero h1{position:absolute;top:520px;left:100px;color:#fff;font-size:60px;font-weight:700;letter-spacing:.5px}
.hero-text{top:608px;left:100px;color:#eef1f6;font-size:17px;line-height:1.6}
/* about */
.about h2{position:absolute;top:1100px;left:96px;font-size:40px;line-height:1.27}
.about h4{position:absolute;top:1224px;left:96px;font-size:20px;color:#111;font-family:"Nunito Sans",sans-serif;font-weight:600}
.about p{position:absolute;left:96px;width:505px;font-size:13px;line-height:1.75}
.badge{top:1235px;left:820px;width:76px;height:76px;border-radius:50%;background:var(--navy);border:4px solid #fff;display:flex;align-items:center;justify-content:center}
.badge i{width:22px;height:22px;background:var(--orange);border-radius:50%}
/* services */
.services{top:1559px;left:0;width:1200px;height:648px;background:var(--grey-bg)}
.services h2{position:absolute;top:1655px;left:85px;font-size:40px}
.service-card{position:absolute;top:1769px;height:353px}
.service-card h3{position:absolute;left:30px;top:230px;color:#fff;font-size:23px}
.round-arrow{position:absolute;width:48px;height:48px;border-radius:50%;background:rgba(255,255,255,.22);display:flex;align-items:center;justify-content:center}
/* experts */
.experts-band{top:2207px;left:0;width:1200px;height:385px;background:linear-gradient(90deg,#1c3661,#264877)}
.experts-band h2{position:absolute;top:2318px;left:90px;color:#fff;font-size:40px;line-height:1.27}
.feature-card{position:absolute;top:2321px;width:232px;height:361px;background:#fff;box-shadow:0 8px 24px rgba(20,40,80,.1);text-align:center}
.feature-card h3{font-size:20px;margin-top:100px}
.feature-card p{font-size:14px;line-height:1.8;margin:16px 28px 0}
.feature-card .more{position:absolute;left:0;right:0;top:272px;font-family:"Ubuntu",sans-serif;font-weight:500;font-size:14px;color:var(--navy)}
.feature-card svg{position:absolute;left:96px;top:50px}
/* why */
.why{top:2592px;left:0;width:1200px;height:741px;background:#fff}
.center-title{position:absolute;left:0;width:1200px;text-align:center}
.why-item h4{position:absolute;font-size:20px;color:var(--navy);font-weight:500}
.why-item p{position:absolute;font-size:13px;line-height:1.6;width:210px}
.icon-ring{position:absolute;width:84px;height:84px;border-radius:50%;background:#fff;box-shadow:0 4px 20px rgba(20,40,80,.12);display:flex;align-items:center;justify-content:center}
/* testimonials */
.testimonials{top:3333px;left:0;width:1200px;height:536px;background:var(--navy-deep)}
.quote-card{position:absolute;top:3547px;width:320px;height:216px;background:#2a4670;color:#e8ecf3}
.quote-card p{position:absolute;left:32px;top:36px;width:262px;font-size:13.5px;line-height:1.75}
.quote-card .q{position:absolute;top:0;left:144px;color:var(--orange);font-family:"Ubuntu";font-weight:700;font-size:50px;line-height:.9}
.avatar{position:absolute;left:28px;top:148px;width:48px;height:48px;border-radius:50%;background:linear-gradient(135deg,#8a98ad,#c9d0da)}
.who{position:absolute;left:94px;top:150px;font-family:"Ubuntu";font-size:16px;color:#fff;line-height:1.25}
.who small{display:block;font-size:14px;color:#9fb0c8}
/* contact */
.contact h2{position:absolute;top:3974px;left:103px;font-size:42px;font-weight:700}
.contact h2 span{font-weight:400}
.contact-item{position:absolute;left:104px;display:flex;gap:26px;align-items:flex-start}
.contact-item b{display:block;font-size:12px;color:#1c2a44;font-weight:700}
.contact-item small{font-size:12px;color:#7b8292}
.form-card{top:3976px;left:597px;width:494px;height:570px;background:#fff;border-top:4px solid #8ea4c4;box-shadow:0 10px 30px rgba(20,40,80,.08);z-index:2}
.form-card h3{position:absolute;top:54px;left:38px;font-size:25px;color:#111b2e}
.field-label{position:absolute;font-size:13px;font-weight:700;color:#1c2a44}
.field{position:absolute;border:1px solid #c9ced8;border-radius:22px;font-size:12px;color:#9aa0ab;padding:11px 22px}
/* footer */
.footer-text{color:#e3e8f0;font-size:13px}
.footer-nav a{position:absolute;top:4713px;color:#fff;font-size:13px;font-weight:600}
.social-box{position:absolute;top:4790px;width:22px;height:22px;border:1px solid #c9d2e0;display:flex;align-items:center;justify-content:center}
.social-box i{display:block;width:8px;height:8px;background:#fff}
</style>
</head>
<body>

<!-- top bar -->
<div class="abs topbar">
  <span style="left:78px">⏱ Mon-Sat: 09am to 07:30pm</span>
  <span style="left:326px">✉ hello@wellpathmail.com</span>
  <span style="left:886px">Faqs</span>
  <span style="left:953px">Pricing</span>
  <div class="social-dot" style="left:1035px"></div>
  <div class="social-dot" style="left:1062px"></div>
  <div class="social-dot" style="left:1090px"></div>
  <div class="social-dot" style="left:1118px"></div>
</div>

<!-- header -->
<div class="abs header">
  <div class="brand" style="left:90px;top:30px;font-size:24px;color:var(--navy)"><i></i>Wellpath Ledgers</div>
  <svg class="abs" style="left:362px;top:38px" width="38" height="34" viewBox="0 0 38 34" fill="none" stroke="#1f3c68" stroke-width="2"><path d="M4 14c0-6 30-6 30 0l-4 3-5-3v-2H13v2l-5 3z"/><rect x="8" y="18" width="22" height="12" rx="2"/><circle cx="19" cy="24" r="3"/></svg>
  <div class="contact-chip" style="left:412px;top:30px">+1-555-014-2200<small>Need help? Make a Call</small></div>
  <svg class="abs" style="left:664px;top:36px" width="36" height="36" viewBox="0 0 36 36" fill="none" stroke="#1f3c68" stroke-width="2"><circle cx="18" cy="18" r="14"/><path d="M4 18h28M18 4c-6 8-6 20 0 28M18 4c6 8 6 20 0 28"/></svg>
  <div class="contact-chip" style="left:711px;top:30px">USA<small>48 Harbor Lane, Suite 2</small></div>
  <div class="btn" style="left:958px;top:30px;width:180px;height:48px;background:var(--navy);border-radius:4px;font-size:13px;font-weight:700">Free Estimate
    <svg width="20" height="20" viewBox="0 0 20 20" fill="none" stroke="#fff" stroke-width="1.6"><circle cx="10" cy="10" r="8"/><path d="M6 10h8M11 7l3 3-3 3"/></svg></div>
</div>

<!-- nav -->
<nav class="abs nav">
  <a class="active" style="left:86px">Home</a>
  <a style="left:197px">About Us</a>
  <a style="left:311px">Services</a>
  <a style="left:448px">Solutions</a>
  <a style="left:560px">Team</a>
  <a style="left:660px">Gallery</a>
  <a style="left:760px">Contact Us</a>
</nav>
<div class="abs phone-box">
  <svg width="40" height="40" viewBox="0 0 40 40" fill="none" stroke="#f7a21b" stroke-width="2"><path d="M10 6l6 1 2 7-4 3c2 5 5 8 10 10l3-4 7 2 1 6c-1 3-4 4-7 3C17 31 9 23 6 13c-1-3 1-6 4-7z"/></svg>
</div>

<!-- hero -->
<section class="abs hero" role="img" aria-label="Clinician reviewing patient records in a laboratory, under a dark blue overlay"></section>
<svg class="abs" style="top:800px;left:0" width="1200" height="160" viewBox="0 0 1200 160">
  <path d="M0 120 C320 105 700 80 1200 0 V160 H0 Z" fill="#fff"/>
  <path d="M0 125 C200 130 500 110 690 95 C500 120 250 150 0 148 Z" fill="#f7a21b"/>
</svg>
<div class="abs hero-tag">We are leaders in</div>
<div class="hero"><h1 style="position:absolute;top:364px;left:100px">Medical Registries Services</h1></div>
<div class="abs hero-text">Lorem ipsum dolor sit amet, consectetur adipiscing elit,<br>sed do eiusmod tempor i</div>
<div class="btn" style="left:100px;top:689px;width:176px;height:51px;font-weight:700">Read More</div>

<!-- about -->
<section class="about">
  <div class="eyebrow" style="top:1063px;left:96px">Who we are</div>
  <h2>Insightful Data,<br>Better Outcomes</h2>
  <h4>Revolutionizing Eye Health Management</h4>
  <p style="top:1270px">Lorem ipsum dolor sit amet, consectetur adipiscing elit, sed do eiusmod temp or incididunt ut labore et dolore magna aliqua. Ut enim ad minim veniam, quis laboris nisi ut aliquip ex ea commodo consequat.</p>
  <p style="top:1345px">Lorem ipsum dolor sit amet, consectetur adipiscing elit, sed do eiusmod temp or incididunt ut labore et dolore magna aliqua.</p>
  <div class="btn" style="left:96px;top:1431px;width:154px;height:45px">Contact us
    <svg width="18" height="14" viewBox="0 0 18 14" fill="none" stroke="#fff" stroke-width="1.8"><path d="M1 7h15M11 2l5 5-5 5"/></svg></div>
  <div class="photo" style="left:618px;top:1046px;width:235px;height:423px;background:linear-gradient(160deg,#c9d3de,#7f94ab 60%,#4d6480)" role="img" aria-label="Doctor consulting with an older patient"></div>
  <div class="photo" style="left:871px;top:1074px;width:233px;height:428px;background:linear-gradient(160deg,#dfe6ec,#8fb0c4 55%,#3f6b8b)" role="img" aria-label="Nurse in blue scrubs using a tablet"></div>
  <div class="abs badge"><i></i></div>
</section>

<!-- services -->
<section class="abs services"></section>
<div class="eyebrow" style="top:1619px;left:89px">Our services</div>
<section class="services-inner">
  <h2 style="position:absolute;top:1655px;left:85px;font-size:40px">Services We Provide</h2>
  <div class="abs" style="top:1670px;left:942px;font-size:14px;color:#2b3345">More Services</div>
  <div class="abs" style="top:1660px;left:1076px;width:38px;height:38px;background:var(--orange);display:flex;align-items:center;justify-content:center">
    <svg width="10" height="14" viewBox="0 0 10 14" fill="none" stroke="#fff" stroke-width="2"><path d="M2 2l5 5-5 5"/></svg></div>
  <div class="service-card" style="left:96px;width:317px;background:linear-gradient(180deg,#b9a590 0%,#6b7d96 50%,#2c4b7c 100%)" role="img" aria-label="Doctor reviewing charts in a clinic">
    <h3>Health Analytics</h3><div class="round-arrow" style="left:24px;top:276px"><svg width="16" height="14" viewBox="0 0 16 14" fill="none" stroke="#fff" stroke-width="1.6"><path d="M1 7h13M9 2l5 5-5 5"/></svg></div></div>
  <div class="service-card" style="left:441px;width:318px;background:linear-gradient(180deg,#d8dde3 0%,#7f93ad 50%,#2c4b7c 100%)" role="img" aria-label="Analyst working with data on screens">
    <h3>Data Management</h3><div class="round-arrow" style="left:24px;top:276px"><svg width="16" height="14" viewBox="0 0 16 14" fill="none" stroke="#fff" stroke-width="1.6"><path d="M1 7h13M9 2l5 5-5 5"/></svg></div></div>
  <div class="service-card" style="left:789px;width:317px;background:linear-gradient(180deg,#9fb3c6 0%,#6d88a8 50%,#2c4b7c 100%)" role="img" aria-label="Care team meeting around a table">
    <h3>Outcome Monitoring</h3><div class="round-arrow" style="left:24px;top:276px"><svg width="16" height="14" viewBox="0 0 16 14" fill="none" stroke="#fff" stroke-width="1.6"><path d="M1 7h13M9 2l5 5-5 5"/></svg></div></div>
</section>

<!-- why bg -->
<section class="abs why"></section>

<!-- experts -->
<section class="abs experts-band"><h2 style="top:111px">Leading<br>Experts</h2></section>
<div class="btn" style="left:92px;top:2486px;width:154px;height:47px">Contact us
  <svg width="18" height="14" viewBox="0 0 18 14" fill="none" stroke="#fff" stroke-width="1.8"><path d="M1 7h15M11 2l5 5-5 5"/></svg></div>
<div class="feature-card" style="left:355px">
  <svg width="40" height="40" viewBox="0 0 40 40" fill="none" stroke="#f7a21b" stroke-width="2"><circle cx="20" cy="13" r="7"/><path d="M6 36c0-8 6-12 14-12s14 4 14 12z"/></svg>
  <h3>Professionalism</h3><p>Lorem ipsum dolor sit consectetur adipiscing elit, sed do eiusmod tempor incididunt</p><div class="more">Read More →</div></div>
<div class="feature-card" style="left:612px">
  <svg width="40" height="40" viewBox="0 0 40 40" fill="none" stroke="#f7a21b" stroke-width="2"><circle cx="20" cy="22" r="15"/><path d="M20 22l7-7M20 9v3M9 22h3M28 22h3"/></svg>
  <h3>Available 24/7</h3><p>Lorem ipsum dolor sit consectetur adipiscing elit, sed do eiusmod tempor incididunt</p><div class="more">Read More →</div></div>
<div class="feature-card" style="left:873px">
  <svg width="40" height="40" viewBox="0 0 40 40" fill="none" stroke="#f7a21b" stroke-width="2"><path d="M14 4l8 4-6 12-8-4zM12 20l-4 10h22M22 26c5 0 10 3 10 9M18 12l8 12"/></svg>
  <h3>Experts</h3><p>Lorem ipsum dolor sit consectetur adipiscing elit, sed do eiusmod tempor incididunt</p><div class="more">Read More →</div></div>

<!-- why choose us -->
<div class="eyebrow" style="top:2738px;left:0;width:1200px;text-align:center">Our services</div>
<h2 class="center-title" style="top:2780px;font-size:40px">Why Choose Us</h2>
<svg class="abs" style="left:340px;top:2880px" width="520" height="380" viewBox="0 0 520 380" fill="none" stroke="#c4c9d2" stroke-width="1.5">
  <path d="M56 110 C25 160 25 220 56 270"/><path d="M464 110 C495 160 495 220 464 270"/>
</svg>
<div class="photo" style="left:434px;top:2906px;width:326px;height:326px;border-radius:50%;background:radial-gradient(circle at 50% 40%,#4a6ea3,#1f3c68 75%)" role="img" aria-label="Smiling consultant in a grey suit with arms crossed"></div>
<div class="photo" style="left:520px;top:2866px;width:154px;height:366px;border-radius:77px 77px 0 0;background:linear-gradient(180deg,#6b7787,#9aa3ad 40%,#8a94a0)" role="img" aria-label="Consultant portrait, upper body"></div>

<div class="why-item">
  <h4 style="top:2912px;left:150px">Global Reach</h4><p style="top:2942px;left:150px">Lorem ipsum dolor sit amet, consectetur adipiscing</p>
  <h4 style="top:3036px;left:118px">Cost-Effective</h4><p style="top:3066px;left:118px">Lorem ipsum dolor sit amet, consectetur adipiscing</p>
  <h4 style="top:3160px;left:131px">Client-Centric</h4><p style="top:3190px;left:131px">Lorem ipsum dolor sit amet, consectetur adipiscing</p>
  <h4 style="top:2902px;left:877px">Regulatory Compliance</h4><p style="top:2932px;left:877px">Lorem ipsum dolor sit amet, consectetur adipiscing</p>
  <h4 style="top:3036px;left:900px">Collaborative Approach</h4><p style="top:3066px;left:900px">Lorem ipsum dolor sit amet, consectetur adipiscing</p>
  <h4 style="top:3160px;left:877px">Industry Recognition</h4><p style="top:3190px;left:877px">Lorem ipsum dolor sit amet, consectetur adipiscing</p>
</div>
<div class="icon-ring" style="left:352px;top:2903px"><svg width="30" height="30" viewBox="0 0 30 30" fill="none" stroke="#f7a21b" stroke-width="1.6"><circle cx="15" cy="10" r="4"/><circle cx="6" cy="13" r="3"/><circle cx="24" cy="13" r="3"/><path d="M8 26c0-5 3-8 7-8s7 3 7 8"/></svg></div>
<div class="icon-ring" style="left:319px;top:3027px"><svg width="30" height="30" viewBox="0 0 30 30" fill="none" stroke="#f7a21b" stroke-width="1.6"><circle cx="15" cy="15" r="12"/><path d="M10 18c3 3 7 3 10 0M10 11h2M18 11h2"/></svg></div>
<div class="icon-ring" style="left:352px;top:3151px"><svg width="30" height="30" viewBox="0 0 30 30" fill="none" stroke="#f7a21b" stroke-width="1.6"><circle cx="15" cy="16" r="10"/><path d="M15 10v6l4 3M8 5l-3 3M22 5l3 3"/></svg></div>
<div class="icon-ring" style="left:760px;top:2903px"><svg width="30" height="30" viewBox="0 0 30 30" fill="none" stroke="#f7a21b" stroke-width="1.6"><path d="M11 3l7 3-5 10-6-3zM9 16l-4 9h19M17 20c4 0 8 2 8 6"/></svg></div>
<div class="icon-ring" style="left:796px;top:3027px"><svg width="30" height="30" viewBox="0 0 30 30" fill="none" stroke="#f7a21b" stroke-width="1.6"><path d="M15 3l3.5 8 8.5.8-6.5 5.6 2 8.3L15 21l-7.5 4.7 2-8.3L3 11.8l8.5-.8z"/></svg></div>
<div class="icon-ring" style="left:760px;top:3151px"><svg width="30" height="30" viewBox="0 0 30 30" fill="none" stroke="#f7a21b" stroke-width="1.6"><circle cx="15" cy="15" r="5"/><path d="M15 3v4M15 23v4M3 15h4M23 15h4M6.5 6.5l3 3M20.5 20.5l3 3M6.5 23.5l3-3M20.5 9.5l3-3"/></svg></div>

<!-- testimonials -->
<section class="abs testimonials"></section>
<div class="eyebrow" style="top:3389px;left:0;width:1200px;text-align:center;color:var(--orange)">Testimonials</div>
<h2 class="center-title" style="top:3428px;font-size:40px;color:#fff">What Clients are Saying</h2>
<div class="quote-card" style="left:92px"><div class="q">❞</div><p>Lorem ipsum dolor sit amet, consectetur adipiscing elit, sed do eiusmod tempor i ncididunt ut labore et dolore magna aliq ua. Ut enim ad minim veniam, quis nostr</p><div class="avatar" role="img" aria-label="Client portrait"></div><div class="who">Dana R.<small>Australia</small></div></div>
<div class="quote-card" style="left:441px"><div class="q">❞</div><p>Lorem ipsum dolor sit amet, consectetur adipiscing elit, sed do eiusmod tempor i ncididunt ut labore et dolore magna aliq ua. Ut enim ad minim veniam, quis nostr</p><div class="avatar" role="img" aria-label="Client portrait"></div><div class="who">Dana R.<small>Australia</small></div></div>
<div class="quote-card" style="left:787px"><div class="q">❞</div><p>Lorem ipsum dolor sit amet, consectetur adipiscing elit, sed do eiusmod tempor i ncididunt ut labore et dolore magna aliq ua. Ut enim ad minim veniam, quis nostr</p><div class="avatar" role="img" aria-label="Client portrait"></div><div class="who">Dana R.<small>Australia</small></div></div>
<svg class="abs" style="left:560px;top:3782px" width="80" height="20" viewBox="0 0 80 20"><g fill="#c8d1de"><circle cx="10" cy="10" r="3.5"/><circle cx="24" cy="10" r="3.5"/><circle cx="54" cy="10" r="3.5"/><circle cx="68" cy="10" r="3.5"/></g><circle cx="39" cy="10" r="4" fill="#f7a21b"/><circle cx="39" cy="10" r="7" fill="none" stroke="#f7a21b"/></svg>

<!-- contact -->
<svg class="abs" style="left:0;top:4330px" width="1200" height="511" viewBox="0 0 1200 511">
  <path d="M0 215 C220 140 430 110 600 95 V0 H1200 V511 H0 Z" fill="#1f3c68"/>
  <path d="M1090 8 H1200 V38 H1090 Z" fill="#f7a21b"/>
  <path d="M390 60 C460 48 530 40 600 30 V40 C530 48 460 56 390 64 Z" fill="#f7a21b"/>
  <path d="M1090 8 C1130 0 1170 0 1200 4 V8 Z" fill="#f7a21b"/>
</svg>
<section class="contact">
  <h2>Contact Us <span>Today</span></h2>
  <div class="contact-item" style="top:4052px">
    <svg width="40" height="36" viewBox="0 0 40 36" fill="none" stroke="#f7a21b" stroke-width="1.6"><path d="M8 4l6 1 2 6-3 3c2 4 5 7 9 9l3-3 6 2 1 6c-1 3-4 4-7 3C16 28 8 20 5 11c-1-3 0-6 3-7z"/></svg>
    <div><b>HEAD OFFICE</b><small>48 Harbor Lane, Riverton</small></div></div>
  <div class="contact-item" style="top:4122px">
    <svg width="40" height="36" viewBox="0 0 40 36" fill="none" stroke="#f7a21b" stroke-width="1.6"><rect x="4" y="8" width="32" height="22" rx="2"/><path d="M4 10l16 11 16-11"/></svg>
    <div><b>EMAIL ADDRESS</b><small>care@wellpathmail.com</small></div></div>
  <div class="contact-item" style="top:4191px">
    <svg width="40" height="40" viewBox="0 0 40 40" fill="none" stroke="#1f3c68" stroke-width="1.6"><path d="M20 36s-11-12-11-20a11 11 0 0 1 22 0c0 8-11 20-11 20z"/><circle cx="20" cy="16" r="4"/></svg>
    <div><b>CALL US NOW</b><small>Call Now: 555-014-2200</small></div></div>
</section>

<div class="abs form-card">
  <h3>Send Us A Message</h3>
  <div class="field-label" style="top:118px;left:38px">First Name</div>
  <div class="field-label" style="top:118px;left:251px">Last Name</div>
  <div class="field" style="top:135px;left:40px;width:197px;height:42px">John</div>
  <div class="field" style="top:135px;left:253px;width:197px;height:42px">Doe</div>
  <div class="field-label" style="top:204px;left:38px">Email</div>
  <div class="field" style="top:223px;left:40px;width:414px;height:42px">info@wellpathmail.com</div>
  <div class="field-label" style="top:294px;left:38px">Message</div>
  <div class="field" style="top:311px;left:40px;width:414px;height:123px;border-radius:0">Type Your Message</div>
  <div class="btn" style="top:475px;left:40px;width:152px;height:45px">Contact us
    <svg width="18" height="14" viewBox="0 0 18 14" fill="none" stroke="#fff" stroke-width="1.8"><path d="M1 7h15M11 2l5 5-5 5"/></svg></div>
</div>

<!-- footer -->
<div class="brand" style="left:146px;top:4598px;font-size:30px;color:#fff"><i></i>Wellpath Ledgers</div>
<svg class="abs" style="left:432px;top:4621px" width="30" height="30" viewBox="0 0 30 30" fill="none" stroke="#fff" stroke-width="1.5"><circle cx="15" cy="15" r="12"/><path d="M3 15h24M15 3c-5 6-5 18 0 24M15 3c5 6 5 18 0 24"/></svg>
<div class="abs footer-text" style="left:471px;top:4616px;line-height:1.45">48 Harbor Lane, Suite 2<br>Riverton, ST 10482</div>
<svg class="abs" style="left:688px;top:4620px" width="26" height="32" viewBox="0 0 26 32" fill="none" stroke="#fff" stroke-width="1.5"><rect x="6" y="3" width="14" height="26" rx="2"/><path d="M11 25h4"/></svg>
<div class="abs footer-text" style="left:726px;top:4616px;line-height:1.45">PHONE<br>(555) 014 2200</div>
<svg class="abs" style="left:864px;top:4622px" width="30" height="26" viewBox="0 0 30 26" fill="none" stroke="#fff" stroke-width="1.5"><rect x="3" y="4" width="24" height="18" rx="1"/><path d="M3 5l12 9 12-9"/></svg>
<div class="abs footer-text" style="left:905px;top:4616px;line-height:1.45">EMAIL<br>info@wellpathmail.com</div>
<div class="abs" style="left:146px;top:4688px;width:920px;height:1px;background:rgba(255,255,255,.12)"></div>
<nav class="footer-nav">
  <a style="left:276px">HOME</a><a style="left:370px">SERVICES</a><a style="left:477px">ABOUT US</a>
  <a style="left:596px">TESTIMONIALS</a><a style="left:746px">BLOG</a><a style="left:840px">CONTACT US</a>
</nav>
<div class="abs" style="left:148px;top:4795px;font-size:11px;color:#c9d2e0">Wellpath Ledgers</div>
<div class="social-box" style="left:935px"><i></i></div>
<div class="social-box" style="left:967px"><i></i></div>
<div class="social-box" style="left:1000px"><i></i></div>
<div class="social-box" style="left:1033px"><i></i></div>

</body>
</html>
```